Basic / Quick Business Card

Quick easy design project!

Need a one sided basic business card that matches font & style of brand and bottle label for our gourmet condiment, Velvet Corwin Sauce. Velvet Corwin Sauce is sold in specialty retail, gourmet groceries and appears on chef-driven restaurant menus, so the target market is a high end, gourmet, artisan-made food-loving customer.

Files Included:
Sauce Bottle Label
Velvet Corwin Sauce Round Logos

**About the logos - the logo may be used in a circle or alone vertically as on side of the bottle label**

Layout of Card:
May be vertical or horizontal based on designer ideas.

Logo usage (in circle vs. stand alone vertical logo) is up to designers descretion as well.

Reverse side of business card will be various high end / professional product photos / food shots using us.zelk.com system. **Designer on this project will NOT design a reserve for the card.**

Paper that will be used for printing:
Zelk Classic - it's a WHITE paper, but we use a cream background on Velvet Corwin Sauce branding, so please take this into account on design to stay brand consistent.

Elements & Copy for Card:
1. Logo in either script horizontal or vertical version
2. Copy: "Artisan Made - Small Batch"
3. Name - Rory Whitlock
4. Title - Creator
5. Phone - xxx.xxx.xxxx
6. xxxx@velvetcorwin.com
7. URL: velvetcorwinsauce.com
8. Social Media: @getvelvetcorwin on Twitter / Facebook / Instagram

Please provide final files in Illustrator or InDesign format.

```html
<!DOCTYPE html>
<html lang="en">
<head>
<meta charset="utf-8">
<title>Velvet Corwin Sauce — Business Card</title>
<link rel="stylesheet" href="https://fonts.googleapis.com/css2?family=Arvo:wght@400;700&display=swap">
<style>
  :root {
    --backdrop: #e4e2dc;
    --cream: #eceadc;
    --cream-shade: #e2e0d2;
    --ink: #2b2a27;
    --charcoal: #2a2622;
    --gold: #d9a227;
    --label-cream: #f3ecd2;
  }
  html, body {
    margin: 0;
    width: 1200px;
    height: 900px;
    overflow: hidden;
    background: var(--backdrop);
    font-family: "Arvo", Georgia, serif;
  }
  .card {
    position: absolute;
    left: 150px;
    top: 193px;
    width: 900px;
    height: 514px;
    background: linear-gradient(160deg, var(--cream), var(--cream-shade));
    box-shadow: 0 8px 24px rgba(0,0,0,.18);
    overflow: hidden;
    color: var(--ink);
  }
  .guide-h {
    position: absolute;
    left: 0; right: 0;
    top: 130px;
    border-top: 2px dotted var(--gold);
  }
  .guide-v {
    position: absolute;
    top: 0; bottom: 0;
    left: 160px;
    border-left: 2px dotted var(--gold);
  }
  .brand-mark {
    position: absolute;
    left: 40px;
    top: 50px;
    width: 200px;
    height: 200px;
    border-radius: 50%;
    background: var(--charcoal);
    display: flex;
    align-items: center;
    justify-content: center;
    text-align: center;
  }
  .brand-name {
    color: var(--gold);
    font-weight: 700;
    font-size: 27px;
    line-height: 1.15;
  }
  .person {
    position: absolute;
    right: 44px;
    top: 72px;
    text-align: right;
  }
  .person-name {
    font-size: 40px;
    font-weight: 400;
    margin: 0;
    line-height: 1;
    letter-spacing: .5px;
  }
  .person-title {
    color: var(--gold);
    font-size: 19px;
    margin-top: 18px;
  }
  .contact {
    position: absolute;
    left: 178px;
    top: 300px;
    list-style: none;
    margin: 0;
    padding: 0;
    font-size: 20px;
    line-height: 30px;
  }
  .contact li { display: flex; align-items: center; gap: 14px; }
  .contact svg { width: 16px; height: 16px; fill: var(--ink); flex: none; }
  .social-handle {
    position: absolute;
    left: 178px;
    top: 418px;
    font-size: 22px;
  }
  .tagline-band {
    position: absolute;
    left: 600px;
    right: 0;
    top: 398px;
    height: 56px;
    background: var(--gold);
    color: var(--label-cream);
    display: flex;
    align-items: center;
    justify-content: center;
    font-size: 21px;
    font-weight: 700;
    letter-spacing: 6px;
  }
</style>
</head>
<body>
  <div class="card">
    <div class="guide-h"></div>
    <div class="guide-v"></div>

    <div class="brand-mark">
      <span class="brand-name">Velvet<br>Corwin</span>
    </div>

    <div class="person">
      <h1 class="person-name">Rory Whitlock</h1>
      <div class="person-title">Creator</div>
    </div>

    <ul class="contact">
      <li>
        <svg viewBox="0 0 16 16" aria-hidden="true"><path d="M3.5 1l2.5 3-1.5 1.5c.8 2 2.5 3.7 4.5 4.5L10.5 8.5l3 2.5-1.5 3C6 14 2 10 2 2.5z"/></svg>
        xxx.xxx.xxxx
      </li>
      <li>
        <svg viewBox="0 0 16 16" aria-hidden="true"><path d="M1 3h14v10H1zM2.5 4.5v.4L8 9l5.5-4.1v-.4z"/></svg>
        xxxx@velvetcorwin.com
      </li>
      <li>
        <svg viewBox="0 0 16 16" aria-hidden="true"><path d="M8 1.5L1 8h2v6.5h4v-4h2v4h4V8h2z"/></svg>
        velvetcorwinsauce.com
      </li>
    </ul>

    <div class="social-handle">@getvelvetcorwin</div>

    <div class="tagline-band">SMALL BATCH</div>
  </div>
</body>
</html>
```